Mix one color into exisiting design, look premium

I have my existing designs, 7 packages. But I want to combine one color inside those designs. I want them to look fit perfectly and look expensive. Premium Products.

You may add anything or change design, make sure to mix the color.

Remember: Your task is to mix the color into my each one of the pakaging designs. Make into new design, look premium for baby products.

```html
<!DOCTYPE html>
<html lang="en">
<head>
<meta charset="utf-8">
<title>Lulu &amp; Bean Baby Diapers – Packaging Range</title>
<link href="https://fonts.googleapis.com/css2?family=Fredoka:wght@500;600&family=Lilita+One&family=M+PLUS+Rounded+1c:wght@700&display=swap" rel="stylesheet">
<style>
  :root{
    --page:#ffffff;
    --tile:#b3b3b3;
    --mint:#9fe3d6;
    --mint-strong:#6fd3c2;
    --glow:#e6ffb0;
    --ink:#2a1c1a;
    --brand-red:#e5343b;
    --peach:#fdc594;
    --lilac:#b493d8;
    --rose:#f7a8bf;
    --sky:#8fd1f6;
    --lemon:#fdd332;
    --tangerine:#f39220;
    --lime:#b6da6c;
  }
  *{box-sizing:border-box;margin:0;padding:0}
  html,body{width:1200px;height:858px;overflow:hidden;background:var(--page)}
  .range{position:relative;width:1200px;height:858px}
  .tile{position:absolute;background:var(--tile)}
  .bag{
    position:absolute;overflow:hidden;
    background:var(--bag);
    border-radius:calc(var(--u)*2.5);
    font-family:"Fredoka",sans-serif;color:var(--ink);
  }
  .bag .seal{position:absolute;left:0;top:0;width:100%;height:2.2%;background:var(--mint-strong)}
  .bag .handle{position:absolute;left:40%;top:5%;width:20%;height:3.6%;border-radius:calc(var(--u)*4);background:rgba(0,0,0,.14)}
  .bag .mini-brand{position:absolute;left:8%;top:5.2%;font-weight:600;color:var(--brand-red);font-size:calc(var(--u)*4.2);line-height:1}
  .bag .mini-brand span{display:block;font-family:"M PLUS Rounded 1c",sans-serif;font-size:calc(var(--u)*2.6);margin-top:calc(var(--u)*.6)}
  .bag .mini-title{position:absolute;right:8%;top:5%;font-family:"Lilita One",sans-serif;font-size:calc(var(--u)*4.2);line-height:1.05;color:var(--ink)}
  .bag .wave{position:absolute;inset:0;width:100%;height:100%}
  .bag .character{position:absolute;border-radius:calc(var(--u)*18) 0 0 calc(var(--u)*18)}
  .bag .brand{position:absolute;text-align:center;color:var(--brand-red);font-weight:600;line-height:1}
  .bag .brand .dot{display:inline-block;width:.45em;height:.45em;border-radius:50%;background:var(--mint-strong);margin-right:.2em;vertical-align:middle}
  .bag .brand span{display:block;font-family:"M PLUS Rounded 1c",sans-serif;font-size:.45em;color:var(--ink);margin-top:.25em}
  .bag .title{position:absolute;font-family:"Lilita One",sans-serif;line-height:.95;letter-spacing:.02em;color:var(--ink)}
  .bag .title .jp{font-family:"M PLUS Rounded 1c",sans-serif;font-size:.32em;display:inline-block;line-height:1.05;vertical-align:top;margin-left:.25em;letter-spacing:0}
  .bag .feature{position:absolute;background:var(--mint-strong);color:#fff;font-weight:500;border-radius:calc(var(--u)*1);white-space:nowrap;letter-spacing:.04em}
  .bag .spec{position:absolute;font-weight:500;white-space:nowrap;color:var(--ink)}
  .bag .icon{position:absolute}
</style>
</head>
<body>
<main class="range">

  <!-- Newborn / peach -->
  <div class="tile" style="left:67px;top:69px;width:280px;height:308px"></div>
  <section class="bag" style="--bag:var(--peach);--u:1.83px;left:114px;top:110px;width:183px;height:231px">
    <div class="seal"></div><div class="handle"></div>
    <div class="mini-brand">Lulu &amp; Bean<span>ルルとビーン</span></div>
    <div class="mini-title">BABY<br>DIAPERS</div>
    <svg class="wave" viewBox="0 0 100 100" preserveAspectRatio="none" aria-hidden="true"><path d="M0 70 C20 40 50 30 100 8 L100 40 C70 50 40 70 0 100Z" fill="var(--mint)"/><path d="M20 96 C30 70 50 50 95 15" stroke="var(--glow)" stroke-width="1.4" fill="none"/></svg>
    <div class="character" role="img" aria-label="Cartoon chick mascot wearing a small crown" style="left:56%;top:26%;width:44%;height:50%;background:linear-gradient(160deg,#fff6b8,#f8e27a)"></div>
    <div class="brand" style="left:8%;top:29%;font-size:calc(var(--u)*8)"><i class="dot"></i>Lulu &amp; Bean<span>ルルとビーン</span></div>
    <div class="title" style="left:12%;top:67%;font-size:calc(var(--u)*10)">BABY<span class="jp">のおむつ<br>赤ちゃん</span><br>DIAPERS</div>
    <div class="feature" style="left:12%;top:85%;font-size:calc(var(--u)*3);padding:calc(var(--u)*.8) calc(var(--u)*2)">BREATHABLE SURFACE LAYER</div>
    <div class="spec" style="left:12%;top:91.5%;font-size:calc(var(--u)*3.4)">NB-code | ≤5kg | 70PCS | UNISEX</div>
  </section>

  <!-- XL / lilac -->
  <div class="tile" style="left:410px;top:71px;width:186px;height:307px"></div>
  <section class="bag" style="--bag:var(--lilac);--u:1.25px;left:440px;top:99px;width:125px;height:254px">
    <div class="seal"></div><div class="handle"></div>
    <div class="mini-brand">Lulu &amp; Bean<span>ルルとビーン</span></div>
    <div class="mini-title">BABY<br>DIAPERS</div>
    <svg class="wave" viewBox="0 0 100 100" preserveAspectRatio="none" aria-hidden="true"><path d="M0 30 C40 25 80 35 100 40 L100 100 L0 100Z" fill="var(--mint)" opacity=".85"/><ellipse cx="60" cy="45" rx="42" ry="28" fill="none" stroke="var(--glow)" stroke-width="2"/></svg>
    <div class="character" role="img" aria-label="Cartoon frog mascot with crown and big smile" style="left:30%;top:27%;width:70%;height:42%;background:linear-gradient(160deg,#b7e58f,#7fc16a)"></div>
    <div class="brand" style="left:8%;top:17%;font-size:calc(var(--u)*10)"><i class="dot"></i>Lulu &amp; Bean<span>ルルとビーン</span></div>
    <div class="title" style="left:8%;top:74%;font-size:calc(var(--u)*13)">BABY<span class="jp">のおむつ<br>赤ちゃん</span><br>DIAPERS</div>
    <div class="feature" style="left:8%;top:86%;font-size:calc(var(--u)*4);padding:calc(var(--u)*.8) calc(var(--u)*2.5)">360° HIP PROTECTION</div>
    <div class="spec" style="left:8%;top:91.5%;font-size:calc(var(--u)*4.6)">XL-code | 12-17kg | 42PCS | UNISEX</div>
  </section>

  <!-- XXL / rose -->
  <div class="tile" style="left:647px;top:70px;width:172px;height:308px"></div>
  <section class="bag" style="--bag:var(--rose);--u:1.17px;left:674px;top:93px;width:117px;height:263px">
    <div class="seal"></div><div class="handle"></div>
    <div class="mini-brand">Lulu &amp; Bean<span>ルルとビーン</span></div>
    <div class="mini-title">BABY<br>DIAPERS</div>
    <svg class="wave" viewBox="0 0 100 100" preserveAspectRatio="none" aria-hidden="true"><path d="M0 18 C40 14 80 18 100 22 L100 88 C60 86 30 90 0 92Z" fill="var(--mint)" opacity=".8"/><ellipse cx="55" cy="52" rx="48" ry="32" fill="none" stroke="var(--glow)" stroke-width="2"/></svg>
    <div class="character" role="img" aria-label="Cartoon white rabbit mascot waving, with crown" style="left:0;top:24%;width:62%;height:60%;border-radius:0 calc(var(--u)*18) calc(var(--u)*18) 0;background:linear-gradient(160deg,#ffffff,#f4ecef)"></div>
    <div class="brand" style="left:40%;top:14%;font-size:calc(var(--u)*10)"><i class="dot"></i>Lulu &amp; Bean<span>ルルとビーン</span></div>
    <div class="title" style="left:38%;top:71%;font-size:calc(var(--u)*13)">BABY<span class="jp">のおむつ<br>赤ちゃん</span><br>DIAPERS</div>
    <div class="feature" style="left:40%;top:83.5%;font-size:calc(var(--u)*4.2);padding:calc(var(--u)*.8) calc(var(--u)*2.5)">360° HIP PROTECTION</div>
    <div class="spec" style="left:22%;top:89.5%;font-size:calc(var(--u)*4.6)">XXL-code | ≥15kg | 38PCS | UNISEX</div>
  </section>

  <!-- Small / sky -->
  <div class="tile" style="left:877px;top:69px;width:257px;height:310px"></div>
  <section class="bag" style="--bag:var(--sky);--u:1.67px;left:924px;top:111px;width:167px;height:226px">
    <div class="seal"></div><div class="handle"></div>
    <div class="mini-brand">Lulu &amp; Bean<span>ルルとビーン</span></div>
    <div class="mini-title">BABY<br>DIAPERS</div>
    <svg class="wave" viewBox="0 0 100 100" preserveAspectRatio="none" aria-hidden="true"><path d="M0 10 C40 30 70 40 100 60 L100 100 L40 100 C30 70 10 40 0 35Z" fill="var(--mint)" opacity=".6"/><path d="M5 12 C50 30 70 50 40 98" stroke="var(--glow)" stroke-width="1.6" fill="none"/></svg>
    <div class="character" role="img" aria-label="Cartoon panda mascot winking, with crown and heart bubble" style="left:0;top:24%;width:38%;height:56%;border-radius:0 calc(var(--u)*18) calc(var(--u)*18) 0;background:linear-gradient(160deg,#ffffff,#3a3552)"></div>
    <div class="brand" style="left:52%;top:28%;font-size:calc(var(--u)*7.2)"><i class="dot"></i>Lulu &amp; Bean<span>ルルとビーン</span></div>
    <div class="title" style="left:42%;top:64%;font-size:calc(var(--u)*10)">BABY<span class="jp">のおむつ<br>赤ちゃん</span><br>DIAPERS</div>
    <div class="feature" style="left:44%;top:81.5%;font-size:calc(var(--u)*3);padding:calc(var(--u)*.8) calc(var(--u)*2)">BREATHABLE SURFACE LAYER</div>
    <div class="spec" style="left:28%;top:88.5%;font-size:calc(var(--u)*3.4)">S-code | 4-8kg | 66PCS | UNISEX</div>
  </section>

  <!-- Large / lemon -->
  <div class="tile" style="left:95px;top:449px;width:203px;height:307px"></div>
  <section class="bag" style="--bag:var(--lemon);--u:1.32px;left:134px;top:480px;width:132px;height:248px">
    <div class="seal"></div><div class="handle"></div>
    <div class="mini-brand">Lulu &amp; Bean<span>ルルとビーン</span></div>
    <div class="mini-title">BABY<br>DIAPERS</div>
    <svg class="wave" viewBox="0 0 100 100" preserveAspectRatio="none" aria-hidden="true"><path d="M0 55 C40 45 70 60 100 50 L100 80 C60 95 30 85 0 90Z" fill="var(--mint)" opacity=".85"/><path d="M55 5 C100 40 90 70 10 95" stroke="var(--glow)" stroke-width="1.8" fill="none"/></svg>
    <div class="character" role="img" aria-label="Cartoon baby elephant mascot with crown" style="left:0;top:34%;width:58%;height:40%;border-radius:0 calc(var(--u)*18) calc(var(--u)*18) 0;background:linear-gradient(160deg,#9dc6f0,#5b8fd6)"></div>
    <div class="brand" style="left:42%;top:24%;font-size:calc(var(--u)*9.5)"><i class="dot"></i>Lulu &amp; Bean<span>ルルとビーン</span></div>
    <div class="title" style="left:40%;top:74%;font-size:calc(var(--u)*11.5)">BABY<span class="jp">のおむつ<br>赤ちゃん</span><br>DIAPERS</div>
    <div class="feature" style="left:40%;top:85.5%;font-size:calc(var(--u)*3.6);padding:calc(var(--u)*.8) calc(var(--u)*2.5)">360° HIP PROTECTION</div>
    <div class="spec" style="left:26%;top:91%;font-size:calc(var(--u)*4)">L-code | 9-14kg | 46PCS | UNISEX</div>
  </section>

  <!-- XXXL / tangerine -->
  <div class="tile" style="left:356px;top:449px;width:335px;height:308px"></div>
  <section class="bag" style="--bag:var(--tangerine);--u:2.61px;left:394px;top:486px;width:261px;height:235px">
    <div class="seal"></div><div class="handle"></div>
    <div class="mini-brand">Lulu &amp; Bean<span>ルルとビーン</span></div>
    <div class="mini-title">BABY<br>DIAPERS</div>
    <svg class="wave" viewBox="0 0 100 100" preserveAspectRatio="none" aria-hidden="true"><path d="M0 55 C25 50 35 40 55 45 C75 50 85 35 100 40 L100 70 C70 80 40 70 0 75Z" fill="var(--mint)" opacity=".85"/><path d="M5 80 C20 55 60 55 95 40" stroke="var(--glow)" stroke-width="1.6" fill="none"/></svg>
    <div class="character" role="img" aria-label="Cartoon giraffe mascot chewing a leaf, with crown" style="left:62%;top:30%;width:38%;height:70%;border-radius:calc(var(--u)*10) 0 0 0;background:linear-gradient(160deg,#fff0a8,#f6c244)"></div>
    <div class="brand" style="left:10%;top:28%;font-size:calc(var(--u)*7)"><i class="dot"></i>Lulu &amp; Bean<span>ルルとビーン</span></div>
    <div class="title" style="left:10%;top:55%;font-size:calc(var(--u)*8.5)">BABY<span class="jp">のおむつ<br>赤ちゃん</span><br>DIAPERS</div>
    <div class="feature" style="left:10%;top:75%;font-size:calc(var(--u)*3.3);padding:calc(var(--u)*.8) calc(var(--u)*2)">360° HIP PROTECTION</div>
    <div class="spec" style="left:10%;top:84%;font-size:calc(var(--u)*3.4)">XXXL-code | 7-12kg | 32PCS | UNISEX</div>
  </section>

  <!-- Medium / lime -->
  <div class="tile" style="left:746px;top:450px;width:230px;height:307px"></div>
  <section class="bag" style="--bag:var(--lime);--u:1.5px;left:787px;top:493px;width:150px;height:241px">
    <div class="seal"></div><div class="handle"></div>
    <div class="mini-brand">Lulu &amp; Bean<span>ルルとビーン</span></div>
    <div class="mini-title">BABY<br>DIAPERS</div>
    <svg class="wave" viewBox="0 0 100 100" preserveAspectRatio="none" aria-hidden="true"><path d="M10 20 C30 10 60 15 70 30 C80 50 60 80 20 90 L0 90 L0 35Z" fill="var(--mint)" opacity=".55"/><path d="M45 8 C10 30 10 70 60 88" stroke="var(--glow)" stroke-width="1.6" fill="none"/></svg>
    <div class="character" role="img" aria-label="Cartoon koala mascot hugging a branch, with crown" style="left:52%;top:24%;width:48%;height:50%;background:linear-gradient(160deg,#a9d4f2,#6ea9de)"></div>
    <div class="brand" style="left:8%;top:23%;font-size:calc(var(--u)*8)"><i class="dot"></i>Lulu &amp; Bean<span>ルルとビーン</span></div>
    <div class="title" style="left:8%;top:69%;font-size:calc(var(--u)*11)">BABY<span class="jp">のおむつ<br>赤ちゃん</span><br>DIAPERS</div>
    <div class="feature" style="left:8%;top:84%;font-size:calc(var(--u)*3.2);padding:calc(var(--u)*.8) calc(var(--u)*2)">SOFT ABSORBENT CORE LAYER</div>
    <div class="spec" style="left:8%;top:90.5%;font-size:calc(var(--u)*3.6)">M-code | 9-14kg | 56PCS | UNISEX</div>
  </section>

</main>
</body>
</html>
```